Business Card Design

Buy and sell properties
Buy and rehab properties
Buy properties for cash
That is what I do but do need a logo
looking for some type of logo or design on it
Just started business
Back of card should say something like BUY HOUSES CASH
Overview: it is a new company. Basically I buy properties wholesale and fix them up and sell them or sell them to other fix and flippers
Background: company is new so not any background
Market: is basically anyone selling a house or buying a house. Someone that needs to sell house fast. Basically I am a cash home buyer!!!

Email on card should be:   harborvalepropertiesinc@example-mail.com

Industry/Entity Type
House
Contact Information for Business Card
Harbor Vale Properties Inc
PO Box 718264
Coral Marsh FL 34197

Dale Morcott
dmorcott@example-mail.com
555-271-9083

```html
<!DOCTYPE html>
<html lang="en">
<head>
<meta charset="utf-8">
<title>Harbor Vale Properties Inc – Business Card</title>
<link href="https://fonts.googleapis.com/css2?family=Open+Sans:wght@400;600;700&display=swap" rel="stylesheet">
<style>
  :root {
    --brand-blue: #1f87c8;
    --brand-blue-deep: #1670b0;
    --card-white: #f4f5f5;
    --ink-blue: #1a6fae;
    --page-bg: #e4e5e6;
    --text-light: #ffffff;
  }
  * { margin: 0; padding: 0; box-sizing: border-box; }
  html, body {
    width: 1200px;
    height: 1000px;
    overflow: hidden;
    background: var(--page-bg);
    font-family: "Open Sans", Arial, sans-serif;
  }
  .card {
    position: absolute;
    left: 250px;
    width: 700px;
    height: 400px;
    overflow: hidden;
    border-radius: 4px;
    box-shadow: 0 2px 6px rgba(0,0,0,0.12);
  }

  /* Back of card */
  .card-back {
    top: 70px;
    background: linear-gradient(160deg, var(--brand-blue-deep), var(--brand-blue));
    color: var(--text-light);
  }
  .card-back .brand {
    position: absolute;
    left: 150px;
    top: 110px;
    display: flex;
    align-items: center;
    gap: 22px;
  }
  .brand-dot {
    flex: none;
    border-radius: 50%;
    background: var(--text-light);
  }
  .card-back .brand-dot { width: 58px; height: 58px; }
  .brand-name {
    font-weight: 600;
    color: var(--text-light);
    line-height: 1.05;
  }
  .card-back .brand-name { font-size: 44px; }
  .card-back .back-email {
    position: absolute;
    left: 0;
    right: 0;
    top: 300px;
    text-align: center;
    font-size: 17px;
    font-weight: 600;
    letter-spacing: 3px;
  }

  /* Front of card */
  .card-front {
    top: 540px;
    background: var(--card-white);
  }
  .card-front .shapes {
    position: absolute;
    inset: 0;
  }
  .band-text {
    position: absolute;
    left: 0;
    width: 470px;
    text-align: center;
    color: var(--text-light);
    font-weight: 600;
  }
  .holder-name { top: 46px; font-size: 24px; font-weight: 700; }
  .holder-phone { top: 104px; font-size: 18px; }
  .holder-email { top: 160px; font-size: 18px; }

  .company-block {
    position: absolute;
    left: 26px;
    top: 254px;
    color: var(--ink-blue);
    font-weight: 600;
    font-size: 12.5px;
    line-height: 1.45;
  }
  .company-block .company-name {
    font-size: 16px;
    font-weight: 700;
    margin-bottom: 6px;
  }

  .card-front .brand {
    position: absolute;
    left: 505px;
    top: 118px;
    display: flex;
    align-items: center;
    gap: 12px;
  }
  .card-front .brand-dot { width: 30px; height: 30px; }
  .card-front .brand-name { font-size: 22px; }

  .tagline {
    position: absolute;
    right: 26px;
    top: 346px;
    color: var(--text-light);
    font-weight: 700;
    font-size: 19px;
    letter-spacing: 5px;
  }
</style>
</head>
<body>

  <section class="card card-back" aria-label="Card back">
    <div class="brand">
      <span class="brand-dot"></span>
      <span class="brand-name">Harbor Vale<br>Properties Inc</span>
    </div>
    <p class="back-email">harborvalepropertiesinc@example-mail.com</p>
  </section>

  <section class="card card-front" aria-label="Card front">
    <svg class="shapes" width="700" height="400" viewBox="0 0 700 400" aria-hidden="true">
      <rect x="0" y="38" width="700" height="46" fill="var(--brand-blue)"/>
      <rect x="0" y="96" width="700" height="42" fill="var(--brand-blue)"/>
      <rect x="0" y="150" width="700" height="46" fill="var(--brand-blue)"/>
      <polygon points="520,0 700,0 700,400 380,400" fill="var(--brand-blue)"/>
    </svg>

    <p class="band-text holder-name">Dale Morcott</p>
    <p class="band-text holder-phone">Phone : 555-271-9083</p>
    <p class="band-text holder-email">Email : dmorcott@example-mail.com</p>

    <div class="company-block">
      <p class="company-name">Harbor Vale Properties Inc</p>
      <p>PO Box 718264</p>
      <p>Coral Marsh FL 34197</p>
      <p>Email : harborvalepropertiesinc@example-mail.com</p>
    </div>

    <div class="brand">
      <span class="brand-dot"></span>
      <span class="brand-name">Harbor Vale<br>Properties Inc</span>
    </div>

    <p class="tagline">BUY HOUSES CASH</p>
  </section>

</body>
</html>
```